I need a design for all my stationary, leaflets, letter heads, business cards, envelopes, compliment slips

this will need my company name, address, telepone numbers, Registered address, company number

i have a few office numbers which i will send you in a file letterhead 3

also 
Name of company is
Brisk Tap.net Ltd
47 Harlow avenue
Burtonwood
Warrington
Cheshire
WA3 7JD

Registered Addressed
4th Floor 62-78 
Mill Bank Road 
London United Kingdom EC2A 9RT

Offices in:-

 Liverpool            0151 555 0143

Manchester       0161555 0172

Ormskirk            01695555018    

St Helens            01744555027

Warrington         01925555039    

Wigan                01942555046    

Southport           01704555053    

Chester              01244 555061

Knutsford           01565555074

Runcorn             01928555082

these are telephone numbers for local northwest offices

if we can present them may be at top of letter head

the o8oo 555 0199 is a free phone number and can be more prominate than the other numbers at the bottom

also next to the address i will get a 0845 number

can please look at incorparating this information

Free Project, plan and design Service

Handy man services
Convert a roof service
Glazing repair service
Lock and window& door repair sercice
Conservatories, Orangeries and glass rooms
windows and doors
Roofline, gutters, fascias and soffits
Bi fold, Sliding and french doors
Drive ways, Paths, Patios and decking
Landscaping and design
Plumbing, Heating, Bathrooms & underfloor heating
Intelegent wiring systems
Extensions, Building and house builds
Joinery

these are the product ranges we are promoting and would like to see may be on a  document 

Company Number:07365492

27 Years Experience watermark or badge some where on the stationary

looking forward to seeing all your designs

Reason: been ill the last 2 days and havnt give it the attention that it requires

cleAN AND SIMPLE DESIGNS IS WHAT IM LOOKING FOR

This is the product range i need to show on the back of the business cards, Compliment slips and on the presentation folders and leaflets

FREE PROJECT PLAN & DESIGN SERVICE

 

HandymanService

Window,Door & conservatory repair service

(Locks,Glazing, Gaskets, letter boxes, hinges and roof repairs)

Create aroom or convert a room service

·Conservatoriesand roof up grading service

·Orangery’s,Lanterns, Tiled roofs rooms

·LOFT& Garage conversions

·Extensions,Renovations, House Builds

Bi folding,French, Sliding patio doors

Windows& Doors

Roofline,Soffits, Gutters and Cladding

Driveways,Paths, Patios, Gravel and decking

Landscaping& design

Plumbing& Heating

Electrician& intelligent wiring projects

Plastering,rendering services

Flooring,Tiling and wooden flooring specialist

I dont believe the product range also should be on the front of the letter heads and possibly should be on the back of the letterheads

At the bottom of the paper work it needs to read the following

Registered in England No.7365492 Registered office 4th Floor,62 - 78 Mill Bank Road, London EC2A 9RT

also need a identity badge with address, Telephone number a place for a picture employee number and company logo on it

im now thinking that the leaflet should be a post card size with poduct range to the rear, with logo, free phone number 

and on the front it should promote our room ranges, Conservatory too hot in summer too cold in winter. 
change your cold CONVERT YOUR ROOF from polycarbaonate roof to an elegant glass roof or to a stunning light weight tiled your and plastered inside

Also another bubble saying
Convert your existing loft or garage space into a room

another bubble saying
Thinking of an Extension, Renovation or house build

another bubble may be  saying
Glass garden rooms and extenions or external garden office 

Im wondering if a letter head with a low shadow of lots of my logo would look any good on the paper work

cheers

confusing why every one has the same brief but the response is so different, good luck i can extend if the designs change but it looks like mind made up time

Thankyou for all the designs, And probably be back in touch for some of the work soon

we are covering all types of customers, we are a home improvement company doing everything to do with the home and garden.

Business

```html
<!DOCTYPE html>
<html lang="en">
<head>
<meta charset="utf-8">
<title>Brisk Tap.net Stationery</title>
<link href="https://fonts.googleapis.com/css2?family=Arimo:wght@400;700&display=swap" rel="stylesheet">
<style>
:root{
  --green:#66d11f;
  --green-dark:#46a514;
  --green-pale:#cdf59c;
  --orange:#f47c20;
  --ink:#111;
  --frame:#555;
  --white:#fff;
}
*{margin:0;padding:0;box-sizing:border-box}
html,body{width:867px;height:1200px;overflow:hidden;background:var(--white)}
body{position:relative;font-family:"Arimo",Arial,sans-serif;color:var(--ink)}
.section-label{position:absolute;font-size:23px;font-weight:400;line-height:1}
.piece{position:absolute;border:1px solid var(--frame);background:var(--white);overflow:hidden}
.piece svg.art{position:absolute;left:0;top:0}
.badge{position:absolute;border-radius:50%;background:radial-gradient(circle at 45% 40%,#f7b45a,#e2741c 60%,#f2a21a 75%,#ffd33d 100%)}
.brand-name{position:absolute;font-family:"Arimo",Arial,sans-serif;font-weight:400;color:var(--green);line-height:1;white-space:nowrap}
.tollfree{position:absolute;color:var(--green);white-space:nowrap}
.reg-band{position:absolute;background:var(--green);color:var(--white);white-space:nowrap;display:flex;align-items:center}
.pill{position:absolute;background:var(--green-dark);color:var(--white);font-weight:700;border-radius:999px;white-space:nowrap;display:flex;align-items:center;justify-content:center;border:1px solid #2f7d0a}
.service-title{position:absolute;color:var(--green-dark);text-align:center;white-space:nowrap}
.range-list{position:absolute;list-style:none;white-space:nowrap}
.range-list .sub{padding-left:1.4em}
.offices{position:absolute;white-space:nowrap}
.id-field{position:absolute;font-size:6.5px;white-space:nowrap}
.photo-box{position:absolute;background:var(--green-dark);border-radius:7px;color:var(--white);font-size:7px;display:flex;align-items:center;justify-content:center}
.envelope-flap{position:absolute;left:615px;top:262px;width:67px;height:276px;background:var(--orange);border:1px solid var(--frame);border-left:none;border-radius:0 22px 22px 0}
</style>
</head>
<body>

<div class="section-label" style="left:5px;top:42px">business cards</div>
<div class="section-label" style="left:5px;top:229px">envelopes</div>
<div class="section-label" style="left:10px;top:563px">compliment slips</div>
<div class="section-label" style="left:5px;top:889px">compliment slips back</div>
<div class="section-label" style="left:697px;top:0">Id Card</div>

<!-- Business card front -->
<div class="piece business-card-front" style="left:5px;top:68px;width:258px;height:149px">
  <svg class="art" width="258" height="149" viewBox="0 0 258 149" aria-hidden="true">
    <path d="M168,0 C210,30 238,75 250,125 L258,125 L258,100 C246,60 222,25 190,0 Z" fill="var(--orange)"/>
    <path d="M190,0 C222,25 246,60 258,100 L258,0 Z" fill="var(--green)"/>
    <rect x="0" y="125" width="258" height="14" fill="var(--green)"/>
  </svg>
  <div class="badge" role="img" aria-label="27 years experience badge with ribbon" style="left:187px;top:14px;width:46px;height:46px"></div>
  <div class="brand-name" style="left:8px;top:52px;font-size:19px">Brisk Tap.net</div>
  <div class="tollfree" style="left:6px;top:112px;font-size:6.5px">Toll free number - 0800 555 0199</div>
  <div class="reg-band" style="left:0;top:125px;width:258px;height:14px;padding-left:6px;font-size:4.6px">Registered in England No.7365492 Registered office 4th Floor,62 - 78 Mill Bank Road, London EC2A 9RT</div>
</div>

<!-- Business card back -->
<div class="piece business-card-back" style="left:276px;top:68px;width:259px;height:149px">
  <svg class="art" width="259" height="149" viewBox="0 0 259 149" aria-hidden="true">
    <rect x="8" y="21" width="251" height="95" fill="var(--green-pale)"/>
    <line x1="160" y1="21" x2="125" y2="116" stroke="var(--white)" stroke-width="0.8"/>
    <path d="M0,0 L20,0 C10,30 4,60 0,100 Z" fill="var(--green)"/>
    <path d="M20,0 L28,0 C14,30 6,60 2,100 L0,100 C4,60 10,30 20,0 Z" fill="var(--orange)"/>
    <line x1="90" y1="19" x2="190" y2="19" stroke="var(--green-dark)" stroke-width="0.4"/>
  </svg>
  <div class="pill" style="left:106px;top:7px;width:50px;height:8px;font-size:3.4px">PRODUCT RANGE</div>
  <div class="service-title" style="left:80px;top:14px;width:100px;font-size:4px">FREE PROJECT PLAN &amp; DESIGN SERVICE</div>
  <ul class="range-list" style="left:22px;top:28px;font-size:3.5px;line-height:7px">
    <li>HandymanService</li>
    <li>Window,Door &amp; conservatory repair service</li>
    <li>(Locks,Glazing, Gaskets, letter boxes, hinges and roof repairs)</li>
    <li>Create aroom or convert a room service</li>
    <li class="sub">·Conservatoriesand roof up grading service</li>
    <li class="sub">·Orangery’s,Lanterns, Tiled roofs rooms</li>
    <li class="sub">·LOFT&amp; Garage conversions</li>
    <li class="sub">·Extensions,Renovations, House Builds</li>
    <li>Bi folding,French, Sliding patio doors</li>
  </ul>
  <ul class="range-list" style="left:166px;top:32px;font-size:3.5px;line-height:7px">
    <li>Windows&amp; Doors</li>
    <li>Roofline,Soffits, Gutters and Cladding</li>
    <li>Driveways,Paths, Patios, Gravel and decking</li>
    <li>Landscaping&amp; design</li>
    <li>Plumbing&amp; Heating</li>
    <li>Electrician&amp; intelligent wiring projects</li>
    <li>Plastering,rendering services</li>
    <li>Flooring,Tiling and wooden flooring specialist</li>
  </ul>
  <div class="offices" style="left:14px;top:117px;font-size:4.5px">Our Offices:</div>
  <div class="offices" style="left:14px;top:125px;font-size:2.9px;line-height:9px">
    Liverpool - 0151 555 0143&nbsp;&nbsp;&nbsp;&nbsp;&nbsp;&nbsp;&nbsp;&nbsp;Manchester - 0161555 0172&nbsp;&nbsp;&nbsp;Ormskirk - 01695555018&nbsp;&nbsp;&nbsp;&nbsp;&nbsp;&nbsp;&nbsp;&nbsp;&nbsp;St Helens - 01744555027&nbsp;&nbsp;&nbsp;Warrington - 01925555039<br>
    Wigan - 01942555046&nbsp;&nbsp;&nbsp;&nbsp;&nbsp;&nbsp;&nbsp;&nbsp;&nbsp;&nbsp;&nbsp;&nbsp;Southport - 01704555053&nbsp;&nbsp;&nbsp;&nbsp;&nbsp;&nbsp;Chester - 01244 555061&nbsp;&nbsp;&nbsp;&nbsp;&nbsp;&nbsp;&nbsp;Knutsford - 01565555074&nbsp;&nbsp;&nbsp;&nbsp;&nbsp;Runcorn - 01928555082
  </div>
</div>

<!-- ID card -->
<div class="piece id-card" style="left:704px;top:22px;width:163px;height:274px">
  <svg class="art" width="163" height="274" viewBox="0 0 163 274" aria-hidden="true">
    <path d="M0,0 L40,0 C18,35 5,75 0,120 Z" fill="var(--green)"/>
    <path d="M40,0 L52,0 C26,35 10,75 3,120 L0,120 C5,75 18,35 40,0 Z" fill="var(--orange)"/>
    <rect x="0" y="245" width="163" height="17" fill="var(--green)"/>
    <g stroke="#777" stroke-width="0.4" stroke-dasharray="0.8 0.8">
      <line x1="70" y1="188" x2="145" y2="188"/>
      <line x1="100" y1="197" x2="145" y2="197"/>
      <line x1="70" y1="206" x2="145" y2="206"/>
      <line x1="70" y1="215" x2="145" y2="215"/>
      <line x1="100" y1="225" x2="145" y2="225"/>
    </g>
  </svg>
  <div class="brand-name" style="left:47px;top:24px;font-size:14px">Brisk Tap.net</div>
  <div class="photo-box" style="left:45px;top:76px;width:71px;height:91px">Photo</div>
  <div class="id-field" style="right:96px;top:183px">Name:</div>
  <div class="id-field" style="right:66px;top:192px">Telephone number:</div>
  <div class="id-field" style="right:96px;top:201px">address:</div>
  <div class="id-field" style="right:66px;top:220px">employee number:</div>
  <div class="reg-band" style="left:0;top:246px;width:163px;height:16px;flex-direction:column;align-items:flex-end;justify-content:center;padding-right:8px;font-size:4.3px;line-height:5.5px">
    <span>Registered in England No.7365492</span>
    <span>Registered office 4th Floor,62 - 78 Mill Bank Road, London EC2A 9RT</span>
  </div>
</div>

<!-- Envelope -->
<div class="envelope-flap" aria-hidden="true"></div>
<div class="piece envelope" style="left:8px;top:258px;width:608px;height:291px">
  <svg class="art" width="608" height="291" viewBox="0 0 608 291" aria-hidden="true">
    <path d="M0,0 L115,0 C55,50 14,150 4,256 L0,256 Z" fill="var(--green)"/>
    <path d="M115,0 L128,0 C70,50 26,150 14,256 L4,256 C14,150 55,50 115,0 Z" fill="var(--orange)"/>
    <rect x="0" y="256" width="608" height="14" fill="var(--green)"/>
  </svg>
  <div class="badge" role="img" aria-label="27 years experience badge with ribbon" style="left:508px;top:30px;width:70px;height:70px"></div>
  <div class="brand-name" style="left:27px;top:188px;font-size:31px">Brisk Tap.net</div>
  <div class="reg-band" style="left:0;top:256px;width:608px;height:14px;padding-left:10px;font-size:7.6px">Registered in England No.7365492 Registered office 4th Floor,62 - 78 Mill Bank Road, London EC2A 9RT</div>
</div>

<!-- Compliment slip front -->
<div class="piece compliment-slip-front" style="left:0;top:597px;width:609px;height:286px">
  <svg class="art" width="609" height="286" viewBox="0 0 609 286" aria-hidden="true">
    <path d="M0,0 L105,0 C45,55 10,150 2,258 L0,258 Z" fill="var(--green)"/>
    <path d="M105,0 L118,0 C58,55 20,150 12,258 L2,258 C10,150 45,55 105,0 Z" fill="var(--orange)"/>
    <rect x="0" y="258" width="609" height="11" fill="var(--green)"/>
    <path d="M603,58 C592,160 560,235 505,286 L520,286 C572,232 602,150 609,50 Z" fill="var(--orange)"/>
    <path d="M609,50 C602,150 572,232 520,286 L609,286 Z" fill="var(--green)"/>
  </svg>
  <div class="badge" role="img" aria-label="27 years experience badge with ribbon" style="left:490px;top:22px;width:68px;height:68px"></div>
  <div class="brand-name" style="left:25px;top:180px;font-size:31px">Brisk Tap.net</div>
  <div class="tollfree" style="left:24px;top:242px;font-size:9px">Toll free number - 0800 555 0199</div>
  <div class="reg-band" style="left:0;top:258px;width:609px;height:11px;padding-left:10px;font-size:7.6px">Registered in England No.7365492 Registered office 4th Floor,62 - 78 Mill Bank Road, London EC2A 9RT</div>
</div>

<!-- Compliment slip back -->
<div class="piece compliment-slip-back" style="left:0;top:913px;width:609px;height:287px">
  <svg class="art" width="609" height="287" viewBox="0 0 609 287" aria-hidden="true">
    <rect x="28" y="55" width="581" height="205" fill="var(--green-pale)"/>
    <line x1="28" y1="56" x2="609" y2="56" stroke="var(--white)" stroke-width="2"/>
    <line x1="28" y1="256" x2="609" y2="256" stroke="var(--white)" stroke-width="2"/>
    <line x1="372" y1="58" x2="258" y2="254" stroke="var(--white)" stroke-width="1.5"/>
    <path d="M0,0 L40,0 C22,70 8,160 3,262 L0,262 Z" fill="var(--green)"/>
    <path d="M40,0 L50,0 C28,60 16,120 12,190 L7,190 C12,120 22,60 40,0 Z" fill="var(--orange)"/>
    <line x1="187" y1="49" x2="417" y2="49" stroke="var(--green-dark)" stroke-width="0.6"/>
    <line x1="0" y1="264" x2="609" y2="264" stroke="var(--green-dark)" stroke-width="0.6"/>
  </svg>
  <div class="pill" style="left:248px;top:12px;width:110px;height:17px;font-size:9px;letter-spacing:0.3px">PRODUCT RANGE</div>
  <div class="service-title" style="left:190px;top:34px;width:226px;font-size:10.2px">FREE PROJECT PLAN &amp; DESIGN SERVICE</div>
  <ul class="range-list" style="left:51px;top:77px;font-size:9.7px;line-height:20px">
    <li>HandymanService</li>
    <li>Window,Door &amp; conservatory repair service</li>
    <li>(Locks,Glazing, Gaskets, letter boxes, hinges and roof repairs)</li>
    <li>Create aroom or convert a room service</li>
    <li class="sub">·Conservatoriesand roof up grading service</li>
    <li class="sub">·Orangery’s,Lanterns, Tiled roofs rooms</li>
    <li class="sub">·LOFT&amp; Garage conversions</li>
    <li class="sub">·Extensions,Renovations, House Builds</li>
    <li>Bi folding,French, Sliding patio doors</li>
  </ul>
  <ul class="range-list" style="left:395px;top:85px;font-size:9.7px;line-height:20px">
    <li>Windows&amp; Doors</li>
    <li>Roofline,Soffits, Gutters and Cladding</li>
    <li>Driveways,Paths, Patios, Gravel and decking</li>
    <li>Landscaping&amp; design</li>
    <li>Plumbing&amp; Heating</li>
    <li>Electrician&amp; intelligent wiring projects</li>
    <li>Plastering,rendering services</li>
    <li>Flooring,Tiling and wooden flooring specialist</li>
  </ul>
</div>

</body>
</html>
```